Confidential Pitch Deck- Moorlink- Peer to Peer Boat Dock and Slip Rentals

We are looking for a redesign for a pitch deck for fund raising purposes. This is for a maritime dock rental company similar to roomzy for private boat and dock slips. The company is called Moorlink.app and is currently in a growth round of funding. We have included an empty version of the deck (no text) and will send the current pitch deck directly designers that we decide to work with. We have placed an example of a deck we like too below as well.

Target Market(s)

Two-sided Market Investors, Boater and Private Dock and Slip Owners

Industry/Entity Type

Peer to Peer property sharing, prop tech

Font styles to use
Serif

Colors
0054AA
0677BA
7BADD7
CADEEF
E8F1F8
FFC000
F8CF3A
FAE287
FDF2CF
FEFAEE

Requirements
Must have
• Our Logo, Our colors, clean text color with vibrant backgrounds
Nice to have
• Boats and boat docks and slips in the same picture in Florida and up and down the east coast

```html
<!DOCTYPE html>
<html lang="en">
<head>
<meta charset="utf-8">
<title>Moorlink — Confidential Pitch Deck</title>
<link rel="stylesheet" href="https://fonts.googleapis.com/css2?family=Lora:wght@500;600;700&family=Source+Serif+4:opsz,wght@8..60,400;8..60,600;8..60,700&display=swap">
<style>
:root{
  --ink:#0054AA;
  --ink-deep:#003d7d;
  --ink-text:#0b2f5c;
  --mid:#0677BA;
  --sky:#7BADD7;
  --mist:#CADEEF;
  --frost:#E8F1F8;
  --accent:#FFC000;
  --accent-soft:#F8CF3A;
  --butter:#FAE287;
  --cream:#FDF2CF;
  --ivory:#FEFAEE;
  --text:#33475e;
  --muted:#7d8b9a;
  --page:#f6f8fb;
  --card:#ffffff;
}
*{box-sizing:border-box;margin:0;padding:0}
html,body{width:1200px;height:2328px;overflow:hidden;background:var(--page)}
body{position:relative;font-family:"Source Serif 4",serif;color:var(--text)}
.slide{position:absolute;width:496px;height:274px;background:var(--card);overflow:hidden;box-shadow:0 14px 28px rgba(0,40,90,.12)}
.col-l{left:84px}.col-r{left:620px}
.abs{position:absolute}
.brand{display:flex;align-items:center;gap:5px;font-family:"Lora",serif;font-weight:700;color:var(--ink);letter-spacing:.08em;text-transform:uppercase}
.brand-dot{border-radius:50%;background:var(--accent);display:inline-block;flex:none}
.title{font-family:"Lora",serif;font-weight:700;color:var(--ink);font-size:14px;white-space:nowrap}
.title.center{left:0;right:0;text-align:center}
.title-rule{position:absolute;width:20px;height:1.5px;background:var(--accent)}
.title-rule.center{left:238px}
.tiny{font-size:4.6px;line-height:7.5px;color:var(--muted)}
.slide-foot{position:absolute;left:0;right:0;bottom:2px;height:10px;display:flex;align-items:center}
.foot-mark{width:9px;height:10px;background:var(--accent)}
.foot-brand{display:flex;align-items:center;gap:3px;padding:0 4px;font-family:"Lora",serif;font-weight:700;font-size:6.4px;letter-spacing:.08em;color:var(--ink);text-transform:uppercase}
.foot-brand .brand-dot{width:8px;height:8px}
.foot-bar{flex:1;height:10px;background:var(--ink);position:relative;color:#fff;font-size:5.6px;line-height:10px}
.foot-url{position:absolute;left:0;right:0;text-align:center}
.foot-page{position:absolute;right:12px}
.photo{position:absolute}
.photo.sea{background:linear-gradient(160deg,#9cc6e4 0%,#4f97c8 35%,#2f7fae 60%,#1f6a97 100%)}
.photo.lake{background:linear-gradient(180deg,#e8f1f8 0%,#b3d0e8 40%,#3f6f9a 55%,#a7c6e0 75%,#cadeef 100%)}
.photo.cove{background:linear-gradient(170deg,#3d8cd0 0%,#6aa8d4 30%,#2f7fb4 65%,#1d6599 100%)}
.photo.sunset{background:linear-gradient(160deg,#fdf2cf 0%,#fae287 30%,#7badd7 60%,#4f8fc2 100%)}
.card{position:absolute;background:var(--card);box-shadow:0 3px 9px rgba(0,40,90,.13)}
.toc-row{position:absolute;width:149px;height:10px;border-bottom:1px solid var(--ink);display:flex;justify-content:space-between;font-size:5.4px;font-weight:600;color:var(--ink-text);text-transform:uppercase;line-height:8px}
.toc-row.active{color:#d89e00;border-color:var(--accent)}
.stat{position:absolute;text-align:center}
.stat-num{font-family:"Lora",serif;font-weight:700;color:var(--ink)}
.stat-rule{width:5px;height:1px;background:var(--ink);margin:2px auto 3px}
.stat.dark{background:linear-gradient(135deg,var(--mid),var(--ink-deep))}
.stat.dark .stat-num,.stat.dark .stat-lab{color:#fff}
.stat.dark .stat-rule{background:var(--accent)}
.stat-lab{color:var(--text)}
.value{position:absolute;width:120px;text-align:center}
.value svg{display:block;margin:0 auto}
.value-name{font-size:5.6px;color:var(--muted);margin-top:2px}
.value-rule{width:7px;height:1px;background:var(--accent);margin:4px auto}
.pro{padding:8px 6px 0}
.pro h4{font-weight:600;font-size:6.6px;color:var(--ink);margin-bottom:4px}
.pro li{list-style:none;font-size:4.6px;line-height:8.6px;color:var(--muted);padding-left:7px;position:relative;white-space:nowrap}
.pro li::before{content:"";position:absolute;left:1px;top:3.5px;width:1.6px;height:1.6px;border-radius:50%;background:var(--accent)}
.adv-badge{position:absolute;width:28px;height:28px;border-radius:50%;background:var(--accent);display:flex;align-items:center;justify-content:center;box-shadow:0 0 0 3px rgba(255,192,0,.3)}
.adv-name{position:absolute;width:132px;text-align:center;font-size:5.8px;font-weight:700;color:var(--ink)}
.adv-text{position:absolute;width:132px;text-align:center;font-size:4.4px;line-height:8.6px;color:var(--muted)}
.kpi{position:absolute;background:#fff;padding:5px 8px}
.kpi-label{font-size:5.4px}
.kpi-value{font-family:"Lora",serif;font-size:14px;font-weight:600;text-align:right;margin-top:6px}
.datum{position:absolute;width:94px;height:38px;background:#fff;box-shadow:0 2px 7px rgba(0,40,90,.1);display:flex;align-items:center;gap:8px;padding-left:8px;border-left:2px solid var(--sky)}
.datum .pct{font-size:8px;color:var(--muted)}
.datum .d-name{font-size:4.8px;font-weight:700;color:var(--ink)}
.datum .d-text{font-size:4.2px;line-height:6px;color:var(--muted)}
.datum.dark{border-color:var(--ink)}.datum.dark .pct{color:var(--ink);font-weight:700}
.datum.warm{border-color:var(--accent)}.datum.warm .pct,.datum.warm .d-name{color:#d89e00}
.bar-row{position:absolute;left:0;height:9px;display:flex;align-items:center}
.bar-label{width:78px;text-align:right;padding-right:4px;font-size:4.4px;color:var(--text);white-space:nowrap}
.bar{height:9px;font-size:4.6px;line-height:9px;padding-left:3px;white-space:nowrap}
.bar.dk{background:var(--sky);color:#fff}.bar.or{background:var(--accent);color:var(--ink-text)}
.step-label{position:absolute;width:80px;text-align:center;font-size:4.8px;font-weight:700;color:var(--ink)}
.step-text{position:absolute;width:80px;text-align:center;font-size:4.2px;line-height:7px;color:var(--muted)}
.closing{background:linear-gradient(180deg,#0677BA 0%,#0054AA 55%,#003d7d 100%)}
.social{position:absolute;width:20px;height:20px;border-radius:50%;background:var(--accent);display:flex;align-items:center;justify-content:center}
</style>
</head>
<body>

<!-- 1 · Cover with image -->
<section class="slide col-l" style="top:80px">
  <div class="photo sea" role="img" aria-label="Aerial view of a waterfront with long wooden docks, moored boats and homes among palm trees" style="inset:0"></div>
  <svg class="abs" style="left:0;top:0" width="496" height="274" viewBox="0 0 496 274" aria-hidden="true">
    <path d="M0 0 H380 C360 70 320 130 250 160 C190 186 150 190 120 210 C85 232 70 250 60 274 H0 Z" fill="#FEFAEE" opacity=".85"/>
  </svg>
  <div class="brand abs" style="left:42px;top:36px;font-size:15px"><span class="brand-dot" style="width:20px;height:20px"></span>Moorlink</div>
  <div class="title abs" style="left:43px;top:88px;font-size:16px">Confidential Pitch Deck</div>
  <div class="abs" style="left:43px;top:110px;font-size:7.4px;color:var(--ink-text)">Business Presentation</div>
  <div class="abs" style="left:43px;top:141px;font-size:8px;font-weight:700;color:var(--ink-text)">Mr. Evan Harlow</div>
</section>

<!-- 2 · Cover plain -->
<section class="slide col-r" style="top:80px">
  <div class="brand abs" style="left:0;right:0;top:85px;justify-content:center;font-size:15px"><span class="brand-dot" style="width:20px;height:20px"></span>Moorlink</div>
  <div class="title center abs" style="top:127px;font-size:16px">Confidential Pitch Deck</div>
  <div class="abs" style="left:0;right:0;text-align:center;top:156px;font-size:7.4px;color:var(--ink-text)">Business Presentation</div>
  <div class="abs" style="left:0;right:0;text-align:center;top:187px;font-size:8px;font-weight:700;color:var(--ink-text)">Mr. Evan Harlow</div>
  <div class="abs" style="left:23px;top:248px;font-size:5.6px;color:var(--text)">January 2023</div>
  <div class="abs" style="right:23px;top:248px;font-size:5.6px;color:var(--text)">moorlink.app</div>
</section>

<!-- 3 · Presentation list -->
<section class="slide col-l" style="top:394px">
  <span class="title-rule center" style="top:12px"></span>
  <h2 class="title center abs" style="top:20px">Presentation List</h2>
  <div class="toc-row" style="left:66px;top:82px"><span>Cover Slides</span><span>01</span></div>
  <div class="toc-row active" style="left:66px;top:118px"><span>Presentation List</span><span>03</span></div>
  <div class="toc-row" style="left:66px;top:154px"><span>About Us</span><span>04</span></div>
  <div class="toc-row" style="left:66px;top:189px"><span>Our Missions &amp; Vision</span><span>06</span></div>
  <div class="toc-row" style="left:281px;top:82px"><span>Infograph One</span><span>07</span></div>
  <div class="toc-row" style="left:281px;top:118px"><span>Infograph Two</span><span>08</span></div>
  <div class="toc-row" style="left:281px;top:154px"><span>Infograph Three</span><span>09</span></div>
  <div class="toc-row" style="left:281px;top:189px"><span>Closing Slides</span><span>10</span></div>
  <footer class="slide-foot"><span class="foot-mark"></span><span class="foot-brand"><span class="brand-dot"></span>Moorlink</span><span class="foot-bar"><span class="foot-url">moorlink.app</span><span class="foot-page">page &nbsp;|&nbsp; 3</span></span></footer>
</section>

<!-- 4 · Vision -->
<section class="slide col-r" style="top:394px">
  <span class="title-rule center" style="top:12px"></span>
  <h2 class="title center abs" style="top:20px">Our Vision</h2>
  <div class="abs tiny" style="left:0;right:0;text-align:center;top:40px">Here Our Subtitle</div>
  <div class="card" style="left:67px;top:74px;width:367px;height:128px;display:flex;align-items:center;justify-content:center;text-align:center;font-size:9.2px;line-height:20px;color:var(--ink-text);padding:0 30px">Lorem ipsum dolor sit amet, consectetuer adipiscing elit. Maecenas porttitor congue massa. Fusce posuere, magna sed pulvinar ultricies, purus lectus malesuada libero.</div>
  <footer class="slide-foot"><span class="foot-mark"></span><span class="foot-brand"><span class="brand-dot"></span>Moorlink</span><span class="foot-bar"><span class="foot-url">moorlink.app</span><span class="foot-page">page &nbsp;|&nbsp; 4</span></span></footer>
</section>

<!-- 5 · About us -->
<section class="slide col-l" style="top:708px">
  <span class="title-rule center" style="top:10px"></span>
  <h2 class="title center abs" style="top:18px">About Us</h2>
  <p class="abs tiny" style="left:60px;right:60px;top:71px;text-align:center;font-size:4.8px;line-height:11px"><b style="color:var(--ink)">Lorem ipsum</b> dolor sit amet, consectetuer adipiscing elit. Maecenas porttitor congue massa. Fusce posuere, magna sed pulvinar ultricies, purus lectus malesuada libero, sit amet commodo magna eros quis urna. Nunc viverra imperdiet enim. Fusce est. Vivamus a tellus. Pellentesque habitant morbi tristique senectus et netus et malesuada.</p>
  <div class="stat card" style="left:33px;top:140px;width:98px;height:60px;padding-top:14px"><div class="stat-num" style="font-size:12px">25+</div><div class="stat-rule"></div><div class="stat-lab" style="font-size:5px">Years Solutions Expertise</div></div>
  <div class="stat card dark" style="left:143px;top:140px;width:98px;height:60px;padding-top:14px"><div class="stat-num" style="font-size:12px">8K</div><div class="stat-rule"></div><div class="stat-lab" style="font-size:5px">Satisfy Costumer</div></div>
  <div class="stat card" style="left:253px;top:140px;width:98px;height:60px;padding-top:14px"><div class="stat-num" style="font-size:12px">7500+</div><div class="stat-rule"></div><div class="stat-lab" style="font-size:5px">Working Hour</div></div>
  <div class="stat card" style="left:363px;top:140px;width:98px;height:60px;padding-top:14px"><div class="stat-num" style="font-size:12px">138</div><div class="stat-rule"></div><div class="stat-lab" style="font-size:5px">Partner Business</div></div>
  <footer class="slide-foot"><span class="foot-mark"></span><span class="foot-brand"><span class="brand-dot"></span>Moorlink</span><span class="foot-bar"><span class="foot-url">moorlink.app</span><span class="foot-page">page &nbsp;|&nbsp; 5</span></span></footer>
</section>

<!-- 6 · Company legacy -->
<section class="slide col-r" style="top:708px">
  <div class="photo sea" role="img" aria-label="Aerial view of two long docks reaching into the water from a wooded shore" style="left:52px;top:60px;width:168px;height:130px;box-shadow:0 3px 9px rgba(0,40,90,.15)"></div>
  <span class="title-rule" style="left:246px;top:62px"></span>
  <h2 class="title abs" style="left:246px;top:72px">The Company Legacy</h2>
  <p class="abs tiny" style="left:246px;top:93px;width:210px">Lorem ipsum dolor sit amet, consectetuer adipiscing elit. Maecenas porttitor congue massa. Fusce posuere, magna sed pulvinar ultricies.</p>
  <div class="stat card" style="left:246px;top:135px;width:48px;height:52px;padding-top:13px"><div class="stat-num" style="font-size:10px">12+</div><div class="stat-rule"></div><div class="stat-lab tiny" style="font-size:3.8px">Partnership</div></div>
  <div class="stat card dark" style="left:297px;top:132px;width:60px;height:55px;padding-top:14px"><div class="stat-num" style="font-size:10px">870+</div><div class="stat-rule"></div><div class="stat-lab" style="font-size:3.8px">Satisfy Customer</div></div>
  <div class="stat card" style="left:358px;top:135px;width:53px;height:52px;padding-top:13px"><div class="stat-num" style="font-size:10px">200+</div><div class="stat-rule"></div><div class="stat-lab tiny" style="font-size:3.8px">Employee</div></div>
  <footer class="slide-foot"><span class="foot-mark"></span><span class="foot-brand"><span class="brand-dot"></span>Moorlink</span><span class="foot-bar"><span class="foot-url">moorlink.app</span><span class="foot-page">page &nbsp;|&nbsp; 6</span></span></footer>
</section>

<!-- 7 · Company values -->
<section class="slide col-l" style="top:1022px">
  <span class="title-rule center" style="top:12px"></span>
  <h2 class="title center abs" style="top:20px">Company Values</h2>
  <div class="card" style="left:185px;top:68px;width:126px;height:82px"></div>
  <div class="value" style="left:37px;top:80px"><svg width="11" height="11" viewBox="0 0 12 12" fill="none" stroke="#0054AA" stroke-width=".9"><rect x="2" y="3" width="8" height="8"/><path d="M4 5h1M7 5h1M4 7h1M7 7h1M5 11V9h2v2M4 3V1h4v2"/></svg><div class="value-name">Value One</div><div class="value-rule"></div><div class="tiny">Lorem ipsum dolor sit amet, consectetuer adipiscing elit.</div></div>
  <div class="value" style="left:188px;top:80px"><svg width="11" height="11" viewBox="0 0 12 12" fill="none" stroke="#0054AA" stroke-width=".9"><path d="M1 5l5-3 5 3M2 5v5h8V5M1 10h10M4 6v3M6 6v3M8 6v3"/></svg><div class="value-name">Value Two</div><div class="value-rule"></div><div class="tiny">Lorem ipsum dolor sit amet, consectetuer adipiscing elit.</div></div>
  <div class="value" style="left:338px;top:80px"><svg width="11" height="11" viewBox="0 0 12 12" fill="none" stroke="#0054AA" stroke-width=".9"><rect x="1" y="1" width="3" height="3"/><rect x="5" y="1" width="3" height="3"/><rect x="1" y="5" width="3" height="3"/><path d="M7 6v5l1.5-1.5L10 11"/></svg><div class="value-name">Value Three</div><div class="value-rule"></div><div class="tiny">Lorem ipsum dolor sit amet, consectetuer adipiscing elit.</div></div>
  <div class="value" style="left:37px;top:170px"><svg width="11" height="11" viewBox="0 0 12 12" fill="none" stroke="#0054AA" stroke-width=".9"><path d="M6 1v6M6 2l3 4H3zM1 8h10l-2 3H3z"/></svg><div class="value-name">Value Four</div><div class="value-rule"></div><div class="tiny">Lorem ipsum dolor sit amet, consectetuer adipiscing elit.</div></div>
  <div class="value" style="left:188px;top:170px"><svg width="11" height="11" viewBox="0 0 12 12" fill="none" stroke="#0054AA" stroke-width=".9"><rect x="2" y="2" width="8" height="9"/><path d="M4 2V1h4v1M4 5h4M4 7h4M4 9h2"/></svg><div class="value-name">Value Five</div><div class="value-rule"></div><div class="tiny">Lorem ipsum dolor sit amet, consectetuer adipiscing elit.</div></div>
  <div class="value" style="left:338px;top:170px"><svg width="11" height="11" viewBox="0 0 12 12" fill="none" stroke="#0054AA" stroke-width=".9"><circle cx="6" cy="6" r="5"/><path d="M1 6h10M6 1c-2.5 3-2.5 7 0 10M6 1c2.5 3 2.5 7 0 10"/></svg><div class="value-name">Value Six</div><div class="value-rule"></div><div class="tiny">Lorem ipsum dolor sit amet, consectetuer adipiscing elit.</div></div>
  <footer class="slide-foot"><span class="foot-mark"></span><span class="foot-brand"><span class="brand-dot"></span>Moorlink</span><span class="foot-bar"><span class="foot-url">moorlink.app</span><span class="foot-page">page &nbsp;|&nbsp; 7</span></span></footer>
</section>

<!-- 8 · Be professional -->
<section class="slide col-r" style="top:1022px">
  <div class="photo lake" role="img" aria-label="Long wooden pier leading across a calm mountain lake" style="left:331px;top:0;width:138px;height:73px"></div>
  <div class="photo cove" role="img" aria-label="Aerial view of a dock extending from a beach cove with houses" style="left:331px;top:80px;width:138px;height:158px"></div>
  <span class="title-rule" style="left:24px;top:50px"></span>
  <h2 class="title abs" style="left:24px;top:58px">Be Professional with Us</h2>
  <p class="abs" style="left:24px;top:82px;width:215px;font-size:4.8px;line-height:11px;color:var(--ink-text)"><b>Lorem ipsum</b> dolor sit amet, consectetuer adipiscing elit. Maecenas porttitor congue massa. Fusce posuere, magna sed pulvinar ultricies.</p>
  <div class="card pro" style="left:24px;top:122px;width:119px;height:84px"><h4>Professional One</h4><ul><li>Lorem ipsum dolor securitee</li><li>Sit amet securitee cam dolor</li><li>Accurating piexama ayen</li><li>Lorem cam rameo oyen</li><li>Remote dekttopa sec</li><li>Compla Securee cameru</li></ul></div>
  <div class="card pro" style="left:148px;top:122px;width:119px;height:84px"><h4>Professional Two</h4><ul><li>Lorem ipsum dolor securitee</li><li>Sit amet securitee cam dolor</li><li>Accurating piexama ayen</li><li>Lorem cam rameo oyen</li><li>Remote dekttopa sec</li><li>Compla Securee cameru</li></ul></div>
  <div class="card pro" style="left:271px;top:122px;width:119px;height:84px"><h4>Professional Three</h4><ul><li>Lorem ipsum dolor securitee</li><li>Sit amet securitee cam dolor</li><li>Accurating piexama ayen</li><li>Lorem cam rameo oyen</li><li>Remote dekttopa sec</li><li>Compla Securee cameru</li></ul></div>
  <footer class="slide-foot"><span class="foot-mark"></span><span class="foot-brand"><span class="brand-dot"></span>Moorlink</span><span class="foot-bar"><span class="foot-url">moorlink.app</span><span class="foot-page">page &nbsp;|&nbsp; 8</span></span></footer>
</section>

<!-- 9 · Our advantage -->
<section class="slide col-l" style="top:1336px">
  <span class="title-rule center" style="top:10px"></span>
  <h2 class="title center abs" style="top:18px">Our Advantage</h2>
  <div class="abs tiny" style="left:0;right:0;text-align:center;top:38px;font-size:5.6px">Lorem ipsum dolor sit amet, consectetuer adipiscing elit.</div>
  <div class="photo sunset" role="img" aria-label="Wooden dock with chairs on a lake at sunrise" style="left:28px;top:66px;width:132px;height:80px"></div>
  <div class="photo sea" role="img" aria-label="Aerial view of docks and boats by a tropical shoreline" style="left:182px;top:66px;width:132px;height:80px"></div>
  <div class="photo lake" role="img" aria-label="Wooden pier stretching into a misty lake" style="left:336px;top:66px;width:132px;height:80px"></div>
  <div class="adv-badge" style="left:80px;top:132px"><svg width="12" height="12" viewBox="0 0 12 12" fill="none" stroke="#fff" stroke-width=".9"><rect x="2" y="3" width="8" height="8"/><path d="M4 5h1M7 5h1M4 7h1M7 7h1M4 3V1h4v2"/></svg></div>
  <div class="adv-badge" style="left:234px;top:132px"><svg width="12" height="12" viewBox="0 0 12 12" fill="none" stroke="#fff" stroke-width=".9"><rect x="1" y="2" width="10" height="7"/><path d="M4 11h4M6 9v2"/></svg></div>
  <div class="adv-badge" style="left:388px;top:132px"><svg width="12" height="12" viewBox="0 0 12 12" fill="none" stroke="#fff" stroke-width=".9"><rect x="2" y="5" width="8" height="6"/><path d="M4 5V3a2 2 0 014 0v2"/></svg></div>
  <div class="adv-name" style="left:28px;top:175px">Advantage One</div>
  <div class="adv-name" style="left:182px;top:175px">Advantage Two</div>
  <div class="adv-name" style="left:336px;top:175px">Advantage Three</div>
  <p class="adv-text" style="left:28px;top:194px">Lorem ipsum dolor sit amet, consectetuer adipiscing elit. Maecenas porttitor congue massa. Fusce posuere, magna sed pulvinar ultricies.</p>
  <p class="adv-text" style="left:182px;top:194px">Lorem ipsum dolor sit amet, consectetuer adipiscing elit. Maecenas porttitor congue massa. Fusce posuere, magna sed pulvinar ultricies.</p>
  <p class="adv-text" style="left:336px;top:194px">Lorem ipsum dolor sit amet, consectetuer adipiscing elit. Maecenas porttitor congue massa. Fusce posuere, magna sed pulvinar ultricies.</p>
  <footer class="slide-foot"><span class="foot-mark"></span><span class="foot-brand"><span class="brand-dot"></span>Moorlink</span><span class="foot-bar"><span class="foot-url">moorlink.app</span><span class="foot-page">page &nbsp;|&nbsp; 9</span></span></footer>
</section>

<!-- 10 · Circle graph -->
<section class="slide col-r" style="top:1336px">
  <span class="title-rule" style="left:32px;top:68px"></span>
  <h2 class="title abs" style="left:32px;top:76px">Circle Graph Analyse</h2>
  <p class="abs tiny" style="left:32px;top:158px;width:150px">Lorem ipsum dolor sit amet, consectetuer adipiscing elit. Maecenas porttitor congue massa. Fusce posuere, magna sed pulvinar ultricies.</p>
  <svg class="abs" style="left:200px;top:60px" width="110" height="110" viewBox="0 0 110 110" aria-label="Donut chart of monthly values">
    <g fill="none" stroke-width="10" transform="rotate(-90 55 55)">
      <circle cx="55" cy="55" r="45" stroke="#FFC000" stroke-dasharray="38 245" stroke-dashoffset="12"/>
      <circle cx="55" cy="55" r="45" stroke="#7BADD7" stroke-dasharray="24 259" stroke-dashoffset="-28"/>
      <circle cx="55" cy="55" r="45" stroke="#F8CF3A" stroke-dasharray="58 225" stroke-dashoffset="-54"/>
      <circle cx="55" cy="55" r="45" stroke="#0054AA" stroke-dasharray="48 235" stroke-dashoffset="-114"/>
      <circle cx="55" cy="55" r="45" stroke="#0677BA" stroke-dasharray="64 219" stroke-dashoffset="-164"/>
      <circle cx="55" cy="55" r="45" stroke="#003d7d" stroke-dasharray="39 244" stroke-dashoffset="-230"/>
    </g>
    <g font-size="5" fill="#fff" font-family="'Source Serif 4',serif" text-anchor="middle">
      <text x="47" y="13">67</text><text x="72" y="17">48</text><text x="96" y="53">89</text><text x="76" y="98">77</text><text x="22" y="87">89</text><text x="12" y="43">67</text>
    </g>
  </svg>
  <div class="abs" style="left:194px;top:174px;font-size:5px;color:var(--mid);white-space:nowrap"><span style="color:var(--ink)">■</span> Jan &nbsp;<span style="color:var(--accent)">■</span> Feb &nbsp;<span style="color:var(--accent)">■</span> Marc &nbsp;<span style="color:var(--accent)">■</span> Apr &nbsp;<span style="color:var(--accent)">■</span> May &nbsp;<span style="color:var(--ink)">■</span> Jun</div>
  <div class="kpi" style="left:356px;top:60px;width:109px;height:55px;border:1px solid var(--accent)"><div class="kpi-label" style="color:#d89e00">June</div><div class="kpi-value" style="color:#d89e00">$5700</div></div>
  <div class="kpi" style="left:356px;top:127px;width:109px;height:56px;border:1px solid var(--ink)"><div class="kpi-label" style="color:var(--ink)">March</div><div class="kpi-value" style="color:var(--ink)">$7600</div></div>
  <footer class="slide-foot"><span class="foot-mark"></span><span class="foot-brand"><span class="brand-dot"></span>Moorlink</span><span class="foot-bar"><span class="foot-url">moorlink.app</span><span class="foot-page">page &nbsp;|&nbsp; 10</span></span></footer>
</section>

<!-- 11 · Pie chart infographic -->
<section class="slide col-l" style="top:1650px">
  <svg class="abs" style="left:48px;top:46px" width="168" height="168" viewBox="0 0 168 168" aria-label="Concentric progress rings">
    <circle cx="84" cy="84" r="80" fill="#fff" stroke="#E8F1F8" stroke-width="6"/>
    <g fill="none" stroke-linecap="round" transform="rotate(-90 84 84)">
      <circle cx="84" cy="84" r="72" stroke="#FFC000" stroke-width="2.5" stroke-dasharray="350 453"/>
      <circle cx="84" cy="84" r="64" stroke="#FFC000" stroke-width="3" stroke-dasharray="300 402" transform="rotate(40 84 84)"/>
      <circle cx="84" cy="84" r="56" stroke="#0054AA" stroke-width="3" stroke-dasharray="270 352" transform="rotate(120 84 84)"/>
      <circle cx="84" cy="84" r="48" stroke="#F8CF3A" stroke-width="3" stroke-dasharray="200 302" transform="rotate(200 84 84)"/>
      <circle cx="84" cy="84" r="40" stroke="#7BADD7" stroke-width="3" stroke-dasharray="160 251" transform="rotate(20 84 84)"/>
    </g>
    <circle cx="84" cy="84" r="19" fill="#0054AA"/>
    <path d="M76 76v16h16M79 88l4-5 3 3 5-7M89 77h2v2" fill="none" stroke="#fff" stroke-width="1.3"/>
  </svg>
  <span class="title-rule" style="left:246px;top:50px"></span>
  <h2 class="title abs" style="left:246px;top:58px">Pie Chart Infographic</h2>
  <p class="abs tiny" style="left:246px;top:79px;width:210px;color:var(--ink-text)">Lorem ipsum dolor sit amet, consectetuer adipiscing elit. Maecenas porttitor congue massa. Fusce posuere, magna sed pulvinar ultricies.</p>
  <div class="datum" style="left:246px;top:126px"><span class="pct">64%</span><div><div class="d-name" style="font-weight:400;color:var(--muted)">Data One</div><div class="d-text">Lorem ipsum dolor sit amet.</div></div></div>
  <div class="datum dark" style="left:355px;top:126px"><span class="pct">68%</span><div><div class="d-name">Data One</div><div class="d-text">Lorem ipsum dolor sit amet.</div></div></div>
  <div class="datum warm" style="left:246px;top:182px"><span class="pct">75%</span><div><div class="d-name">Data One</div><div class="d-text">Lorem ipsum dolor sit amet.</div></div></div>
  <div class="datum warm" style="left:355px;top:182px"><span class="pct" style="font-weight:400">64%</span><div><div class="d-name">Data One</div><div class="d-text">Lorem ipsum dolor sit amet.</div></div></div>
  <footer class="slide-foot"><span class="foot-mark"></span><span class="foot-brand"><span class="brand-dot"></span>Moorlink</span><span class="foot-bar"><span class="foot-url">moorlink.app</span><span class="foot-page">page &nbsp;|&nbsp; 11</span></span></footer>
</section>

<!-- 12 · Bar infographic -->
<section class="slide col-r" style="top:1650px">
  <span class="title-rule center" style="top:12px"></span>
  <h2 class="title center abs" style="top:20px">Pie Chart Infographic</h2>
  <div class="bar-row" style="top:68px"><span class="bar-label">Holdco 1ea</span><span class="bar dk" style="width:228px">$8,040,900</span></div>
  <div class="bar-row" style="top:82px"><span class="bar-label">Nile Finance</span><span class="bar or" style="width:210px">$380,099</span></div>
  <div class="bar-row" style="top:97px"><span class="bar-label">Finance 4R</span><span class="bar dk" style="width:254px">$4,099,009</span></div>
  <div class="bar-row" style="top:111px"><span class="bar-label">Zero Seven Finance</span><span class="bar or" style="width:62px">$3,037,000</span></div>
  <div class="bar-row" style="top:126px"><span class="bar-label">Sixth</span><span class="bar dk" style="width:177px">$2,093,003</span></div>
  <div class="bar-row" style="top:140px"><span class="bar-label">5th Finance</span><span class="bar or" style="width:76px">$10,340</span></div>
  <div class="bar-row" style="top:155px"><span class="bar-label">Finance Zero Four</span><span class="bar dk" style="width:101px">$250,030</span></div>
  <div class="bar-row" style="top:169px"><span class="bar-label">Finance Three</span><span class="bar or" style="width:62px">$610,040</span></div>
  <div class="bar-row" style="top:184px"><span class="bar-label">Finance 2</span><span class="bar dk" style="width:50px">$20,030</span></div>
  <div class="bar-row" style="top:198px"><span class="bar-label">Finance One</span><span class="bar or" style="width:42px">$40,030</span></div>
  <div class="abs" style="left:283px;top:170px;font-size:3.8px;color:var(--muted);line-height:13px"><span style="color:var(--sky)">●</span> Analyse One<br><span style="color:var(--accent)">●</span> Analyse Two</div>
  <div class="card" style="left:365px;top:67px;width:100px;height:61px;padding:12px"><div style="font-size:6.4px;font-weight:700;color:var(--ink)">Analyse One</div><div class="tiny" style="font-size:4px;margin-top:4px">Lorem ipsum dolor sit amet, consectetuer adipiscing elit.</div></div>
  <div class="card" style="left:365px;top:145px;width:100px;height:62px;padding:12px;background:var(--accent)"><div style="font-size:6.4px;font-weight:700;color:var(--ink-text)">Analyse Two</div><div class="tiny" style="font-size:4px;margin-top:4px;color:var(--ink-text)">Lorem ipsum dolor sit amet, consectetuer adipiscing elit.</div></div>
  <footer class="slide-foot"><span class="foot-mark"></span><span class="foot-brand"><span class="brand-dot"></span>Moorlink</span><span class="foot-bar"><span class="foot-url">moorlink.app</span><span class="foot-page">page &nbsp;|&nbsp; 12</span></span></footer>
</section>

<!-- 13 · Infograph steps -->
<section class="slide col-l" style="top:1964px">
  <span class="title-rule center" style="top:12px"></span>
  <h2 class="title center abs" style="top:20px">Infograph</h2>
  <svg class="abs" style="left:0;top:90px" width="496" height="66" viewBox="0 0 496 66" aria-label="Five step process">
    <g stroke="#CADEEF" stroke-width=".7" stroke-dasharray="2 1.5"><path d="M97 33h29M186 33h28M275 33h28M364 33h28"/></g>
    <g fill="#fff" stroke="#CADEEF" stroke-width=".8">
      <path d="M67 3l27 15v30L67 63 40 48V18z"/>
      <path d="M156 3l27 15v30l-27 15-27-15V18z"/>
      <path d="M423 3l27 15v30l-27 15-27-15V18z"/>
      <path d="M334 3l27 15v30l-27 15-27-15V18z"/>
    </g>
    <path d="M245 0l31 17v32L245 66l-31-17V17z" fill="#FEFAEE" stroke="#FFC000" stroke-width="1"/>
    <g font-family="'Source Serif 4',serif" font-size="6" font-weight="700" fill="#0054AA" text-anchor="middle">
      <text x="67" y="35">Step 1</text><text x="156" y="35">Step 2</text><text x="245" y="35" font-size="6.6">Step 3</text><text x="334" y="35">Step 4</text><text x="423" y="35">Step 5</text>
    </g>
  </svg>
  <div class="step-label" style="left:27px;top:181px">Marketing Step</div>
  <div class="step-label" style="left:116px;top:181px">Production Step</div>
  <div class="step-label" style="left:205px;top:181px">R&amp;D Step</div>
  <div class="step-label" style="left:294px;top:181px">Vendor Step</div>
  <div class="step-label" style="left:383px;top:181px">Supplier Step</div>
  <p class="step-text" style="left:27px;top:192px">Lorem ipsum dolor sit amet, consectetuer adipisc. Maecenas porttitor congue.</p>
  <p class="step-text" style="left:116px;top:192px">Lorem ipsum dolor sit amet, consectetuer adipisc. Maecenas porttitor congue.</p>
  <p class="step-text" style="left:205px;top:192px">Lorem ipsum dolor sit amet, consectetuer adipisc. Maecenas porttitor congue.</p>
  <p class="step-text" style="left:294px;top:192px">Lorem ipsum dolor sit amet, consectetuer adipisc. Maecenas porttitor congue.</p>
  <p class="step-text" style="left:383px;top:192px">Lorem ipsum dolor sit amet, consectetuer adipisc. Maecenas porttitor congue.</p>
  <footer class="slide-foot"><span class="foot-mark"></span><span class="foot-brand"><span class="brand-dot"></span>Moorlink</span><span class="foot-bar"><span class="foot-url">moorlink.app</span><span class="foot-page">page &nbsp;|&nbsp; 13</span></span></footer>
</section>

<!-- 14 · Thank you -->
<section class="slide col-r closing" style="top:1964px">
  <h2 class="abs" style="left:0;right:0;text-align:center;top:86px;font-family:'Lora',serif;font-weight:700;font-size:25px;color:#fff">Thank You</h2>
  <svg class="abs" style="left:143px;top:128px" width="210" height="4" viewBox="0 0 210 4" aria-hidden="true"><path d="M0 2 Q105 0 210 2 Q105 4 0 2Z" fill="#FFC000"/></svg>
  <p class="abs" style="left:120px;right:120px;top:139px;text-align:center;font-size:5.4px;line-height:11px;color:#E8F1F8">Lorem ipsum dolor sit amet, consectetuer adipiscing elit. Maecen portion congue massa. Fusce posuere, magna sed pulvinar ultricies.</p>
  <div class="social" style="left:194px;top:196px"><svg width="10" height="10" viewBox="0 0 12 12" fill="none" stroke="#0054AA" stroke-width=".9"><circle cx="6" cy="6" r="5"/><path d="M1 6h10M6 1c-2.5 3-2.5 7 0 10M6 1c2.5 3 2.5 7 0 10"/></svg></div>
  <div class="social" style="left:238px;top:196px"></div>
  <div class="social" style="left:281px;top:196px"></div>
</section>

</body>
</html>
```